Letterhead Design

We are a physical security and protective intelligence firm based in regional NSW, Australia. We are in need of a professionally designed letter head/ document for our company Valtrix Security. Ref. www.valtrixsecurity.com.au for detailed company information. MUST include Master Licence and ABN details.

Target Market(s)

corporate business, celebrities, property managers, entertainment professionals

Industry/Entity Type

Security

Requirements
Must have
• Must look sharp, professional and cutting edge. Think 419, Silent Directorate, QX3/4 and NOT the movie known as "Dwayne Tuffle Lot Patrol". :-)
Should not have
• Please NO cheesy security guards standing around in uniform. Think protective intelligence and counter terrorism operations. We do not wish to convey an image of a guard company, we offer this service but it is not what we aim to promote. Seek to achieve a higher level approach... elite as opposed to "the usual" guard services etc.

```html
<!DOCTYPE html>
<html lang="en">
<head>
<meta charset="utf-8">
<title>Valtrix Security Letterhead</title>
<link href="https://fonts.googleapis.com/css2?family=Open+Sans:wght@400;700&family=Tinos&display=swap" rel="stylesheet">
<style>
  :root {
    --backdrop: #e4e4e4;
    --paper: #ffffff;
    --ink: #1c1c1c;
    --body-ink: #3a3a3a;
    --accent: #2a4a8c;
    --muted: #555555;
    --sig-fill: #f1f1f1;
  }
  * { box-sizing: border-box; margin: 0; padding: 0; }
  html, body { width: 1200px; height: 1057px; overflow: hidden; }
  body { background: var(--backdrop); position: relative; }

  .letterhead {
    position: absolute; left: 240px; top: 20px;
    width: 719px; height: 1017px;
    background: var(--paper);
    box-shadow: 0 2px 10px rgba(0,0,0,.12);
    overflow: hidden;
  }

  .brand { position: absolute; top: 66px; left: 0; width: 100%; text-align: center; }
  .brand-name {
    display: inline-flex; align-items: center; gap: 10px;
    font: 700 31px/1 "Open Sans", sans-serif; color: var(--ink); letter-spacing: -0.5px;
    text-transform: uppercase;
  }
  .brand-square { width: 14px; height: 14px; background: var(--accent); display: inline-block; }
  .brand-rule { width: 268px; height: 2px; margin: 7px auto 4px; background: linear-gradient(90deg, transparent, var(--accent), transparent); }
  .brand-tagline { font: 400 13.5px/1.2 "Open Sans", sans-serif; color: var(--ink); }

  .letter-body {
    position: absolute; top: 244px; left: 92px; width: 553px;
    font: 400 15.4px/19.6px "Tinos", serif; color: var(--body-ink);
    text-align: justify; hyphens: auto;
  }
  .letter-body p { margin-bottom: 19.6px; }

  .sign-off { position: absolute; top: 796px; left: 92px; font: 400 15.4px/19.6px "Tinos", serif; color: var(--body-ink); }
  .signature { position: absolute; top: 822px; left: 84px; width: 150px; height: 38px; background: var(--sig-fill); border-radius: 4px; }
  .signer { position: absolute; top: 866px; left: 92px; font: 400 15px/1 "Tinos", serif; color: var(--muted); }

  .letter-footer {
    position: absolute; top: 944px; left: 0; width: 100%; text-align: center;
    font: 400 10.4px/14px "Open Sans", sans-serif; color: var(--ink);
  }
  .letter-footer .item { display: inline-flex; align-items: center; gap: 4px; margin: 0 4px; }
  .letter-footer svg { width: 9px; height: 9px; fill: var(--ink); }
  .letter-footer .sep { margin: 0 6px; }
</style>
</head>
<body>
  <main class="letterhead">
    <header class="brand">
      <div class="brand-name"><span class="brand-square"></span>Valtrix Security</div>
      <div class="brand-rule"></div>
      <div class="brand-tagline">Precision in Protective Intelligence</div>
    </header>

    <section class="letter-body">
      <p>Lorem ipsum dolor sit amet,</p>
      <p>Lorem ipsum dolor sit amet, consectetur adipiscing elit. Donec orci purus, luctus vitae dignissim eu, iaculis sed purus. Vivamus faucibus, ipsum nec aliquet viverra, leo mauris condimentum ligula, sit amet sagittis enim ligula quis arcu. Nam egestas tortor id nisi porttitor mattis. In tortor ante, ultricies in suscipit a, tempus non massa. Vivamus et auctor mi. Fusce vel massa nulla. Phasellus nec eros mauris, et scelerisque orci. Donec malesuada orci vitae nulla accumsan porta a id massa. Quisque accumsan iaculis magna sit amet fringilla. Maecenas consequat, magna eget tincidunt semper, odio nibh rutrum mi, id feugiat ante nisi eu risus. Vestibulum nunc orci, rhoncus a placerat in, ultricies in mi.</p>
      <p>Quisque scelerisque sagittis nulla at porttitor. Mauris a justo et tellus interdum tristique. Sed id augue vitae urna euismod commodo aliquet a quam. Pellentesque arcu velit, cursus et malesuada ut, rutrum nisi iaculis consequat et diam. Nullam erat sem, rhoncus id ullamcorper vitae, rhoncus et arcu. In ultricies ultricies nulla, ut rutrum nisi iaculis at. Donec eu magna a metus ornare faucibus. Fusce aliquet faucibus ultricies. Morbi semper, est id tincidunt gravida, sem arcu adipiscing lacus, ac bibendum nulla leo eu purus. Quisque nec diam sed risus consectetur a ccumsan quis quis nibh. Vestibulum id purus lorem.</p>
      <p>Vivamus vehicula accumsan lacinia. Aliquam erat volutpat. Pellentesque consequat venenatis velit non gravida. Etiam et sem et nulla congue rutrum nisi iaculis aliquam sed eget augue. Nulla facilisi. Pellentesque habitant morbi tristique senectus et netus et malesuada fames ac turpis egestas. Nulla a elit at sem iaculis congue. Nullam mollis tristique lobortis.</p>
    </section>

    <p class="sign-off">Ipsum dolor,</p>
    <div class="signature" role="img" aria-label="Handwritten signature"></div>
    <p class="signer">John Doe Smith</p>

    <footer class="letter-footer">
      <div><span class="item"><svg viewBox="0 0 10 10"><path d="M5 0a3.6 3.6 0 0 0-3.6 3.6C1.4 6.3 5 10 5 10s3.6-3.7 3.6-6.4A3.6 3.6 0 0 0 5 0zm0 5a1.4 1.4 0 1 1 0-2.8A1.4 1.4 0 0 1 5 5z"/></svg>Kelbrook, New South Wales, Australia, 2351</span></div>
      <div><span class="item"><svg viewBox="0 0 10 10"><path d="M2 0h2l1 2.5-1.3 1a6 6 0 0 0 2.8 2.8l1-1.3L10 6v2a2 2 0 0 1-2 2A8 8 0 0 1 0 2a2 2 0 0 1 2-2z"/></svg>(02) 5550 1183 - 0400 555 328</span></div>
      <div>
        <span class="item"><svg viewBox="0 0 10 10"><path d="M0 2h10v6H0zM0 2l5 3.5L10 2"/></svg>office@valtrixsecurity.com.au</span>
        <span class="item"><svg viewBox="0 0 10 10"><circle cx="5" cy="5" r="5"/></svg>www.valtrixsecurity.com.au</span>
      </div>
      <div>Master Licence: 40000 1182<span class="sep">|</span>ABN: 11 222 333 444<span class="sep">|</span>Association Member: 00 01 20 35</div>
    </footer>
  </main>
</body>
</html>
```